Landingpage design for Carvelotrader website

We need a design for a responsive 1 page landing page.
Good example: https://www.frelvana.com/
On the homepage we will like to have a explanation video
attached you can find the logo's

About the website Carvelo.hub:
Carvelo.hub is a “Broker” we bring buyers and sellers together and facilitate transactions

Simple
quickly
Actuel
Compare (who is the best provider, at what price)
great offer
independent
1 invoice

Target Market(s)

BtoB

Number of Pages Required

1 page

Requirements
Must have
• On the homepage we will like to have a explanation video
Nice to have
• something between shipper and carrier and bring them togheter
• We will focus us first on fish transport... maybe you can add something
• Map from europe that shows our workarea

```html
<!DOCTYPE html>
<html lang="en">
<head>
<meta charset="utf-8">
<title>Carvelo.hub – Landing page</title>
<link href="https://fonts.googleapis.com/css2?family=Montserrat:wght@400;500;600;700&family=Roboto+Condensed:wght@300;400&display=swap" rel="stylesheet">
<style>
:root{
  --blue:#2ea8d9;
  --blue-dark:#0f4f70;
  --ink:#1d1d1f;
  --text-grey:#9a9a9a;
  --band-grey:#eeeeee;
  --white:#ffffff;
}
*{box-sizing:border-box;margin:0;padding:0}
html,body{width:1200px;height:2862px;overflow:hidden}
body{font-family:"Roboto Condensed",sans-serif;color:var(--ink);background:var(--white);position:relative}
section,header,footer{position:absolute;left:0;width:1200px;overflow:hidden}

/* header */
.site-header{top:0;height:69px;background:var(--blue)}
.brand{position:absolute;display:flex;align-items:center;gap:12px;font-family:"Montserrat",sans-serif;font-weight:600;color:var(--white);font-size:22px;letter-spacing:1px}
.brand-dot{width:34px;height:34px;border-radius:50%;border:3px solid var(--white)}
.site-header .brand{left:143px;top:17px}
.main-nav{position:absolute;left:406px;top:27px;display:flex;gap:0}
.main-nav a{font-family:"Montserrat",sans-serif;font-weight:500;font-size:13px;color:var(--white);text-decoration:none;margin-right:30px}
.account{position:absolute;left:845px;top:22px;display:flex;gap:5px}
.account a{display:block;height:26px;line-height:26px;padding:0 15px;border-radius:13px;background:var(--blue-dark);color:var(--white);font-family:"Montserrat",sans-serif;font-size:12px;font-weight:500;text-decoration:none}
.header-divider{position:absolute;left:1009px;top:0;width:1px;height:69px;background:rgba(255,255,255,.45)}
.menu-toggle{position:absolute;left:1028px;top:24px}

/* hero */
.hero{top:69px;height:397px;background:linear-gradient(180deg,#f7f7f7,#e2e2e2)}
.hero-question{position:absolute;left:143px;display:flex;gap:14px;align-items:flex-start}
.hero-question .q-icon{margin-top:6px}
.hero-question h2{font-family:"Montserrat",sans-serif;font-weight:500;font-size:25px;line-height:25px;color:var(--ink)}
.hero-question h2 strong{display:block;font-weight:700;font-size:29px;line-height:30px}
.hero-lead{position:absolute;left:143px;top:192px;width:320px;font-size:16px;line-height:24px;color:#333}
.free-badge{position:absolute;left:143px;top:250px;width:311px;height:45px;border-radius:23px;background:var(--blue);color:var(--white);font-family:"Montserrat",sans-serif;font-weight:500;font-size:26px;line-height:45px;text-align:center}
.free-badge strong{font-weight:700}
.hero-media{position:absolute;left:511px;top:8px;width:689px;height:389px;background:linear-gradient(90deg,#e7e7e7 0%,#c8b9a6 35%,#d8cbb8 60%,#e4e4e4 80%,#cfd3d6 100%)}
.play-button{position:absolute;left:714px;top:170px}

/* call-to-action */
.cta{position:absolute;display:flex;align-items:center;gap:24px;font-size:15px;line-height:17px;color:#222}
.cta p{width:230px}

/* feature bands */
.band-grey{background:var(--band-grey)}
.band-white{background:var(--white)}
.feature-title{position:absolute;font-family:"Montserrat",sans-serif;font-weight:600;font-size:27px;line-height:28px;color:var(--ink)}
.feature-title small{display:block;font-size:19px;font-weight:500;line-height:22px}
.feature-text{position:absolute;width:440px;font-size:15.5px;line-height:22px;color:var(--text-grey);font-weight:300}
.pill{position:absolute;width:557px;height:271px;border:4px solid var(--blue);padding:10px}
.pill-left{left:0;border-left:none;border-radius:0 136px 136px 0;padding-left:0}
.pill-right{left:643px;border-right:none;border-radius:136px 0 0 136px;padding-right:0}
.pill-photo{width:100%;height:100%}
.pill-left .pill-photo{border-radius:0 125px 125px 0}
.pill-right .pill-photo{border-radius:125px 0 0 125px}
.photo-woman{background:linear-gradient(90deg,#d9cfc3,#b99a8c 45%,#e8dfd4)}
.photo-goods{background:linear-gradient(90deg,#d8b891,#e9eef2 50%,#d9b27c)}
.photo-europe{background:radial-gradient(ellipse at 50% 50%,#cfcfcf,#f1f1f1 70%)}
.photo-truck{background:linear-gradient(90deg,#eeeeee,#d9b770 40%,#c8a064 65%,#c95a4a 90%)}
.photo-city-map{background:linear-gradient(110deg,#e9e5da 0%,#e3e0d6 45%,#8fb5e8 55%,#9fc1ee 100%)}

/* footer */
.site-footer{top:2591px;height:271px;background:var(--blue);color:var(--white)}
.site-footer .brand{left:143px;top:60px}
.footer-links{position:absolute;top:60px;list-style:none;font-family:"Montserrat",sans-serif;font-weight:600;font-size:12px;line-height:20px}
.newsletter{position:absolute;left:845px;top:60px;font-family:"Montserrat",sans-serif}
.newsletter h4{font-size:12px;font-weight:600;line-height:20px}
.newsletter .email{margin-top:5px;width:210px;height:34px;background:var(--white);color:#333;font-size:10px;line-height:34px;padding-left:8px}
.newsletter .submit{margin-top:10px;width:82px;height:32px;background:var(--blue-dark);font-size:11px;line-height:32px;text-align:center}
.footer-rule{position:absolute;left:143px;top:206px;width:914px;height:1px;background:rgba(255,255,255,.35)}
.copyright{position:absolute;left:0;top:226px;width:1200px;text-align:center;font-family:"Montserrat",sans-serif;font-weight:600;font-size:12px}
</style>
</head>
<body>

<header class="site-header">
  <div class="brand"><span class="brand-dot"></span>CARVELO.HUB</div>
  <nav class="main-nav"><a href="#">ABOUT US</a><a href="#">PRICING</a><a href="#">FAQ</a><a href="#">CONTACT US</a></nav>
  <div class="account"><a href="#">LOGIN</a><a href="#">REGISTER</a></div>
  <div class="header-divider"></div>
  <svg class="menu-toggle" width="28" height="22" viewBox="0 0 28 22"><g stroke="#fff" stroke-width="2.5" stroke-linecap="round"><line x1="2" y1="3" x2="26" y2="3"/><line x1="6" y1="11" x2="26" y2="11"/><line x1="10" y1="19" x2="26" y2="19"/></g></svg>
</header>

<section class="hero">
  <div class="hero-media" role="img" aria-label="Photo of a smiling business woman and a delivery man holding a cardboard box beside a white truck"></div>
  <svg class="play-button" width="84" height="84" viewBox="0 0 84 84"><circle cx="42" cy="42" r="38" fill="rgba(255,255,255,.25)" stroke="#2ea8d9" stroke-width="3"/><path d="M33 26 L60 42 L33 58 Z" fill="#2ea8d9"/></svg>
  <div class="hero-question" style="top:58px">
    <svg class="q-icon" width="26" height="26" viewBox="0 0 26 26"><circle cx="13" cy="13" r="11.5" fill="none" stroke="#2ea8d9" stroke-width="2"/><text x="13" y="18" text-anchor="middle" font-family="Montserrat,sans-serif" font-size="14" font-weight="600" fill="#2ea8d9">?</text></svg>
    <h2>LOOKING FOR A<strong>TRANSPORT COMPANY?</strong></h2>
  </div>
  <div class="hero-question" style="top:124px">
    <svg class="q-icon" width="26" height="26" viewBox="0 0 26 26"><circle cx="13" cy="13" r="11.5" fill="none" stroke="#2ea8d9" stroke-width="2"/><text x="13" y="18" text-anchor="middle" font-family="Montserrat,sans-serif" font-size="14" font-weight="600" fill="#2ea8d9">?</text></svg>
    <h2>LOOKING FOR A<strong>LOADING?</strong></h2>
  </div>
  <p class="hero-lead">We bring you together and find the best and most efficient way for your shipments.</p>
  <div class="free-badge">Carvelo.hub is <strong>FREE</strong></div>
  <div class="cta" style="left:143px;top:318px">
    <p>You are a view steps away from the easiest way to organize your transport!</p>
    <svg width="46" height="36" viewBox="0 0 46 36"><path d="M4 3 H26 A15 15 0 0 1 26 33 H4" fill="none" stroke="#222" stroke-width="4" stroke-linecap="round"/><path d="M22 11 L29 18 L22 25" fill="none" stroke="#222" stroke-width="3.5" stroke-linecap="round" stroke-linejoin="round"/></svg>
  </div>
</section>

<section class="band-grey" style="top:466px;height:400px">
  <div class="pill pill-left" style="top:64px"><div class="pill-photo photo-woman" role="img" aria-label="Photo of a woman on a sofa holding a tablet"></div></div>
  <h2 class="feature-title" style="left:610px;top:82px"><small>WHY SHOULD I USE</small>CARVELO.HUB?</h2>
  <p class="feature-text" style="left:610px;top:150px">Lorem ipsum dolor sit amet, consectetur adipiscing elit, sed do eiusmod tempor incididunt ut labore et dolore magna aliqua. Ut enim ad minim veniam, quis nostrud exercitation ullamco laboris nisi ut aliquip ex ea commodo consequat. Duis aute irure dolor in reprehenderit in voluptate velit esse cillum dolore.</p>
  <div class="cta" style="left:610px;top:276px">
    <p>You are a view steps away from the easiest way to organize your transport!</p>
    <svg width="46" height="36" viewBox="0 0 46 36"><path d="M4 3 H26 A15 15 0 0 1 26 33 H4" fill="none" stroke="#2ea8d9" stroke-width="4" stroke-linecap="round"/><path d="M22 11 L29 18 L22 25" fill="none" stroke="#2ea8d9" stroke-width="3.5" stroke-linecap="round" stroke-linejoin="round"/></svg>
  </div>
</section>

<section class="band-white" style="top:866px;height:424px">
  <h2 class="feature-title" style="left:143px;top:98px">TRANSPORT SOLUTIONS</h2>
  <p class="feature-text" style="left:143px;top:150px">Lorem ipsum dolor sit amet, consectetur adipiscing elit, sed do eiusmod tempor incididunt ut labore et dolore magna aliqua. Ut enim ad minim veniam, quis nostrud exercitation ullamco laboris nisi ut aliquip ex ea commodo consequat. Duis aute irure dolor in reprehenderit in voluptate velit esse cillum dolore.</p>
  <div class="cta" style="left:143px;top:276px">
    <p>You are a view steps away from the easiest way to organize your transport!</p>
    <svg width="46" height="36" viewBox="0 0 46 36"><path d="M4 3 H26 A15 15 0 0 1 26 33 H4" fill="none" stroke="#2ea8d9" stroke-width="4" stroke-linecap="round"/><path d="M22 11 L29 18 L22 25" fill="none" stroke="#2ea8d9" stroke-width="3.5" stroke-linecap="round" stroke-linejoin="round"/></svg>
  </div>
  <div class="pill pill-right" style="top:75px"><div class="pill-photo photo-goods" role="img" aria-label="Collage of transportable goods: a car, a washing machine, a dog, a sofa and a loader"></div></div>
</section>

<section class="band-grey" style="top:1290px;height:431px">
  <div class="pill pill-left" style="top:80px"><div class="pill-photo photo-europe" role="img" aria-label="Grey relief map of Europe showing the work area"></div></div>
  <h2 class="feature-title" style="left:610px;top:106px">DESTINATION EUROPE</h2>
  <p class="feature-text" style="left:610px;top:158px">Lorem ipsum dolor sit amet, consectetur adipiscing elit, sed do eiusmod tempor incididunt ut labore et dolore magna aliqua. Ut enim ad minim veniam, quis nostrud exercitation ullamco laboris nisi ut aliquip ex ea commodo consequat. Duis aute irure dolor in reprehenderit in voluptate velit esse cillum dolore.</p>
  <div class="cta" style="left:610px;top:284px">
    <p>You are a view steps away from the easiest way to organize your transport!</p>
    <svg width="46" height="36" viewBox="0 0 46 36"><path d="M4 3 H26 A15 15 0 0 1 26 33 H4" fill="none" stroke="#2ea8d9" stroke-width="4" stroke-linecap="round"/><path d="M22 11 L29 18 L22 25" fill="none" stroke="#2ea8d9" stroke-width="3.5" stroke-linecap="round" stroke-linejoin="round"/></svg>
  </div>
</section>

<section class="band-white" style="top:1721px;height:437px">
  <h2 class="feature-title" style="left:143px;top:108px">FREE?</h2>
  <p class="feature-text" style="left:143px;top:160px">Lorem ipsum dolor sit amet, consectetur adipiscing elit, sed do eiusmod tempor incididunt ut labore et dolore magna aliqua. Ut enim ad minim veniam, quis nostrud exercitation ullamco laboris nisi ut aliquip ex ea commodo consequat. Duis aute irure dolor in reprehenderit in voluptate velit esse cillum dolore.</p>
  <div class="cta" style="left:143px;top:286px">
    <p>You are a view steps away from the easiest way to organize your transport!</p>
    <svg width="46" height="36" viewBox="0 0 46 36"><path d="M4 3 H26 A15 15 0 0 1 26 33 H4" fill="none" stroke="#2ea8d9" stroke-width="4" stroke-linecap="round"/><path d="M22 11 L29 18 L22 25" fill="none" stroke="#2ea8d9" stroke-width="3.5" stroke-linecap="round" stroke-linejoin="round"/></svg>
  </div>
  <div class="pill pill-right" style="top:80px"><div class="pill-photo photo-truck" role="img" aria-label="Forklift loading boxes into a red truck trailer"></div></div>
</section>

<section class="band-grey" style="top:2158px;height:433px">
  <div class="pill pill-left" style="top:82px"><div class="pill-photo photo-city-map" role="img" aria-label="Street map of a harbour city with the office location"></div></div>
  <h2 class="feature-title" style="left:610px;top:108px">CONTACT</h2>
  <p class="feature-text" style="left:610px;top:160px">Lorem ipsum dolor sit amet, consectetur adipiscing elit, sed do eiusmod tempor incididunt ut labore et dolore magna aliqua. Ut enim ad minim veniam, quis nostrud exercitation ullamco laboris nisi ut aliquip ex ea commodo consequat. Duis aute irure dolor in reprehenderit in voluptate velit esse cillum dolore.</p>
  <div class="cta" style="left:610px;top:286px">
    <p>You are a view steps away from the easiest way to organize your transport!</p>
    <svg width="46" height="36" viewBox="0 0 46 36"><path d="M4 3 H26 A15 15 0 0 1 26 33 H4" fill="none" stroke="#2ea8d9" stroke-width="4" stroke-linecap="round"/><path d="M22 11 L29 18 L22 25" fill="none" stroke="#2ea8d9" stroke-width="3.5" stroke-linecap="round" stroke-linejoin="round"/></svg>
  </div>
</section>

<footer class="site-footer">
  <div class="brand"><span class="brand-dot"></span>CARVELO.HUB</div>
  <ul class="footer-links" style="left:458px"><li>Company</li><li>About us</li><li>Career</li><li>Blog</li></ul>
  <ul class="footer-links" style="left:658px"><li>Services</li><li>Help</li><li>Locations</li><li>Support</li></ul>
  <div class="newsletter">
    <h4>Newsletter Signup</h4>
    <div class="email">Email Address</div>
    <div class="submit">SUBMIT</div>
  </div>
  <div class="footer-rule"></div>
  <p class="copyright">Copyright © 2017, Carvelo.hub. All rights reserved.</p>
</footer>

</body>
</html>
```